Trade Show Display Background for Alcohol Brand

Velsora (sipvelsora.example) is an espresso martini company. We are participating in a trade show and need a display graphic designed for our booth.

We are going to purchase a backlit display:
https://www.brightpanelco.example/custom-8ft-flat-luminous-tension-fabric-led-backlit-trade-show-display.html

Artwork guidelines are attached.

Booth Design Concept:
Upscale outdoor bar.
This background will be all the way at the back of the booth.

Ivy covered wall that you would find at a upscale roof deck or patio.
Velsora logo looks like a sign on the wall.
A neon sign over the ivy covered wall reads "Espresso Martinis (large) All Day & Night (smaller)"

Large espresso martini layered on top of the background so people can easily tell what our product is. I attached some stock photos for reference, they have not been purchased yet.

Feel free to get creative if you have other ideas.

Requirements
Nice to have
• sipvelsora.example somewhere on the design

```html
<!DOCTYPE html>
<html lang="en">
<head>
<meta charset="utf-8">
<title>Velsora – Espresso Martinis Booth Backdrop</title>
<link rel="stylesheet" href="https://fonts.googleapis.com/css2?family=Marcellus&display=swap">
<style>
  :root {
    --page-bg: #ffffff;
    --backdrop-dark: #140805;
    --backdrop-mid: #2a120c;
    --ivy-tone: #3a1a14;
    --glass-glow: #5a2a16;
    --brand-tan: #b39a78;
    --accent-amber: #f6a83b;
    --text-white: #ffffff;
  }
  * { margin: 0; padding: 0; box-sizing: border-box; }
  html, body {
    width: 681px;
    height: 1200px;
    overflow: hidden;
    background: var(--page-bg);
  }
  .canvas {
    position: relative;
    width: 681px;
    height: 1200px;
  }
  .backdrop {
    position: absolute;
    left: 40px;
    top: 300px;
    width: 600px;
    height: 600px;
    overflow: hidden;
    box-shadow: 2px 6px 10px rgba(0, 0, 0, 0.35);
    font-family: "Marcellus", serif;
  }
  .backdrop-photo {
    position: absolute;
    inset: 0;
    background:
      radial-gradient(ellipse 45% 55% at 80% 45%, var(--glass-glow) 0%, transparent 70%),
      radial-gradient(ellipse 50% 70% at 10% 70%, var(--ivy-tone) 0%, transparent 75%),
      linear-gradient(160deg, var(--backdrop-mid) 0%, var(--backdrop-dark) 60%, var(--backdrop-dark) 100%);
  }
  .brand-name {
    position: absolute;
    left: 52px;
    top: 56px;
    font-size: 82px;
    line-height: 1;
    letter-spacing: -1px;
    color: var(--brand-tan);
    text-transform: uppercase;
  }
  .headline-lead {
    position: absolute;
    left: 55px;
    top: 190px;
    font-size: 62px;
    line-height: 1;
    color: var(--text-white);
  }
  .headline-main {
    position: absolute;
    left: 52px;
    top: 268px;
    font-size: 78px;
    line-height: 1;
    letter-spacing: -3px;
    color: var(--accent-amber);
  }
  .tagline {
    position: absolute;
    left: 55px;
    top: 370px;
    font-size: 36px;
    line-height: 1;
    color: var(--text-white);
  }
  .tagline .amp { color: var(--accent-amber); }
  .website {
    position: absolute;
    left: 54px;
    top: 488px;
    font-size: 22px;
    line-height: 1;
    color: var(--brand-tan);
  }
</style>
</head>
<body>
  <main class="canvas">
    <section class="backdrop">
      <div class="backdrop-photo" role="img" aria-label="Photo of an espresso martini topped with coffee beans on a dark bar, with an ivy-covered wall and warm bokeh lights behind"></div>
      <h1 class="brand-name">Velsora</h1>
      <p class="headline-lead">Espresso</p>
      <p class="headline-main">MARTINIS</p>
      <p class="tagline">ALL DAY <span class="amp">&amp;</span> NIGHT</p>
      <p class="website">sipvelsora.example</p>
    </section>
  </main>
</body>
</html>
```